Australia rare honey label

Australia honey brand: Kelunto honey (dostwin rare honey)
Honey type: Red Gum, Orange bloosom, Black honey, Quince etc
Require obvious color or symble to distingwish above different type or taste

Target Market(s)

preminum customers

Font styles to use
Decorative
Script

Requirements
Nice to have
• unique idea which is not similar to market other honey brands.
There is a label sample reference for some information if want to know what infor need to be filled into labels

```html
<!DOCTYPE html>
<html lang="en">
<head>
<meta charset="utf-8">
<title>Kelunto Honey – Black Honey Label</title>
<link href="https://fonts.googleapis.com/css2?family=Montserrat:wght@300;400;700&family=Roboto+Condensed:wght@400;700&display=swap" rel="stylesheet">
<style>
  :root {
    --page-bg: #f1f1f1;
    --label-dark: #22170e;
    --label-mid: #3a2a1b;
    --cell-tone: #4a3826;
    --gold: #e4ac17;
    --gold-rim: #d8951b;
    --white: #ffffff;
  }
  * { margin: 0; padding: 0; box-sizing: border-box; }
  html, body {
    width: 1200px;
    height: 1165px;
    overflow: hidden;
    background: var(--page-bg);
  }
  .canvas {
    position: relative;
    width: 1200px;
    height: 1165px;
  }
  .label {
    position: absolute;
    left: 286px;
    top: 132px;
    width: 628px;
    height: 900px;
    border-radius: 314px;
    border: 9px solid var(--gold-rim);
    background: linear-gradient(100deg, var(--label-dark) 0%, var(--label-mid) 55%, var(--label-dark) 100%);
    overflow: hidden;
    font-family: "Montserrat", sans-serif;
  }
  .label__texture {
    position: absolute;
    top: 0;
    right: 0;
    width: 62%;
    height: 100%;
    background: linear-gradient(90deg, rgba(74,56,38,0) 0%, var(--cell-tone) 45%, rgba(34,23,14,0.9) 100%);
    opacity: 0.8;
  }
  .brand {
    position: absolute;
    left: 0;
    right: 0;
    top: 110px;
    display: flex;
    align-items: center;
    justify-content: center;
    gap: 14px;
    color: var(--gold);
    font-weight: 700;
    font-size: 46px;
    letter-spacing: 1px;
  }
  .brand__dot {
    width: 30px;
    height: 30px;
    border-radius: 50%;
    background: var(--gold);
  }
  .origin {
    position: absolute;
    left: 52px;
    top: 258px;
    color: var(--gold);
    font-weight: 700;
    font-size: 29px;
    letter-spacing: 0.5px;
  }
  .maker {
    position: absolute;
    left: 52px;
    top: 296px;
    color: var(--white);
    font-weight: 400;
    font-size: 28px;
    letter-spacing: 0.5px;
  }
  .product {
    position: absolute;
    left: 48px;
    top: 390px;
    font-weight: 700;
    font-size: 92px;
    line-height: 1.04;
  }
  .product__tone { display: block; color: var(--gold); }
  .product__kind { display: block; color: var(--white); }
  .claim {
    position: absolute;
    left: 52px;
    top: 602px;
    color: var(--gold);
    font-family: "Roboto Condensed", sans-serif;
    font-weight: 700;
    font-size: 38px;
    line-height: 1.0;
  }
  .weight {
    position: absolute;
    left: 0;
    right: 0;
    top: 780px;
    text-align: center;
    color: var(--white);
    font-family: "Roboto Condensed", sans-serif;
    line-height: 1;
  }
  .weight__value { display: block; font-size: 46px; font-weight: 400; }
  .weight__unit { display: block; font-size: 19px; margin-top: 3px; }
</style>
</head>
<body>
  <main class="canvas">
    <section class="label">
      <div class="label__texture" role="img" aria-label="Honeycomb hexagon pattern in dark bronze tones"></div>
      <div class="brand"><span class="brand__dot"></span><span class="brand__name">Kelunto</span></div>
      <p class="origin">AUSTRALIA</p>
      <p class="maker">KELUNTO HONEY</p>
      <h1 class="product">
        <span class="product__tone">BLACK</span>
        <span class="product__kind">HONEY</span>
      </h1>
      <p class="claim">100% PURE<br>&amp; UNFILTERED</p>
      <p class="weight"><span class="weight__value">500g</span><span class="weight__unit">NTW</span></p>
    </section>
  </main>
</body>
</html>
```